Design a Flyer for Brightway Housekeepers

Design a Flyer for brightway housekeepers

Size: A6 - please organise for WEB and PRINT (template for both adobe photoshop and illustrator attached)

INCLUDE THIS TEXT BELOW:

BRIGHTWAY HOUSEKEEPERS
PERTH'S LEADING RESIDENTIAL CLEANING COMPANY

From your small studio apartment to your large family home, Brightway Housekeepers is the ultimate answer for your cleaning needs. We even do your dishes and washing!

CONTACT US NOW FOR A NO OBLIGATION FREE QUOTE
Find us on Friendloop (friendloop image/logo)
Visit our website: [url removed, login to view]
Phone: 0417 293 518

```html
<!DOCTYPE html>
<html lang="en">
<head>
<meta charset="utf-8">
<title>Brightway Housekeepers – Flyer</title>
<link rel="stylesheet" href="https://fonts.googleapis.com/css2?family=Open+Sans:wdth,wght@75..100,400..800&display=swap">
<style>
  :root {
    --sky-light: #dcEFF8;
    --sky-ray: #2b9fd6;
    --banner-fill: #e6f3fa;
    --ink-blue: #1b6d94;
    --sun-orange: #f6aa3d;
    --cream: #fdf2d2;
    --band-blue: #1c6e95;
    --band-red: #e1313f;
    --bucket-navy: #2d5b87;
    --bottle-lilac: #b99ac8;
    --bottle-blue: #3f8fd0;
  }
  * { margin: 0; padding: 0; box-sizing: border-box; }
  html, body { width: 1200px; height: 859px; overflow: hidden; background: #ffffff; }
  .flyer {
    position: relative;
    width: 1200px;
    height: 859px;
    overflow: hidden;
    font-family: "Open Sans", Arial, sans-serif;
  }
  .sunburst {
    position: absolute;
    inset: 0 0 300px 0;
    background: radial-gradient(ellipse at 50% 75%, var(--sky-light) 0%, #a9d7ee 45%, var(--sky-ray) 100%);
  }
  .hero-art { position: absolute; inset: 0; }
  .banner-title {
    font-stretch: 75%;
    font-weight: 600;
    fill: var(--ink-blue);
  }
  .banner-subtitle {
    font-stretch: 80%;
    font-weight: 700;
    font-size: 37px;
    fill: var(--ink-blue);
  }
  .brand-name {
    font-weight: 700;
    font-size: 38px;
    fill: var(--cream);
  }
  .intro-band {
    position: absolute;
    left: 0; top: 553px;
    width: 1200px; height: 212px;
    background: var(--band-blue);
    color: var(--cream);
    display: flex;
    align-items: center;
    justify-content: center;
  }
  .intro-text {
    width: 1120px;
    font-size: 34px;
    font-stretch: 88%;
    line-height: 53px;
    text-align: center;
    font-weight: 400;
    margin-top: -8px;
  }
  .contact-band {
    position: absolute;
    left: 0; top: 765px;
    width: 1200px; height: 94px;
    background: var(--band-red);
    color: var(--cream);
    text-align: center;
    padding-top: 12px;
  }
  .contact-cta { font-weight: 700; font-size: 17px; line-height: 26px; }
  .contact-details { font-weight: 600; font-size: 18px; line-height: 28px; font-stretch: 92%; }
</style>
</head>
<body>
<main class="flyer">
  <div class="sunburst" role="img" aria-label="Blue sunburst rays radiating behind the banner"></div>

  <svg class="hero-art" width="1200" height="859" viewBox="0 0 1200 859">
    <defs>
      <linearGradient id="bottleTones" x1="0" y1="0" x2="1" y2="0">
        <stop offset="0" stop-color="#2f7a45"/>
        <stop offset="0.35" stop-color="var(--bottle-lilac)"/>
        <stop offset="1" stop-color="var(--bottle-blue)"/>
      </linearGradient>
      <path id="subtitleArc" d="M212,282 Q600,352 1008,282"/>
    </defs>

    <rect x="40" y="300" width="226" height="213" rx="14" fill="var(--bucket-navy)"
          role="img" aria-label="Illustration of a cleaning bucket with gloves and a squeegee"/>
    <rect x="900" y="282" width="272" height="231" rx="14" fill="url(#bottleTones)"
          role="img" aria-label="Illustration of spray bottles and cleaning products"/>

    <path class="ribbon" d="M58,92 Q600,-20 1116,86 L1028,192 L1146,294 Q600,412 40,310 L166,188 Z"
          fill="var(--banner-fill)" stroke="var(--ink-blue)" stroke-width="5" stroke-linejoin="round"/>
    <path d="M80,102 Q600,0 1096,97 L1010,192 L1124,286 Q600,396 64,300 L146,188 Z"
          fill="none" stroke="var(--ink-blue)" stroke-width="2"/>

    <text class="banner-title" x="600" y="180" font-size="165" text-anchor="middle" textLength="632" lengthAdjust="spacing">PERTH'S</text>
    <text class="banner-subtitle">
      <textPath href="#subtitleArc" startOffset="50%" text-anchor="middle">LEADING RESIDENTIAL CLEANING COMPANY</textPath>
    </text>

    <polygon class="roof" points="0,513 600,427 1200,513 1200,553 0,553" fill="var(--sun-orange)"/>
    <text class="brand-name" x="600" y="528" text-anchor="middle" textLength="578" lengthAdjust="spacing">BRIGHTWAY HOUSEKEEPERS</text>
  </svg>

  <section class="intro-band">
    <p class="intro-text">From your small studio apartment to your large family home, Brightway Housekeepers is the ultimate answer for your cleaning needs. We even do your dishes and washing!</p>
  </section>

  <footer class="contact-band">
    <p class="contact-cta">CONTACT US NOW FOR A NO OBLIGATION FREE QUOTE</p>
    <p class="contact-details">Find us on Friendloop (friendloop image/logo)&nbsp; Visit our website: www.brightwayhousekeepers.sitenest.com Phone: 0417 293 518</p>
  </footer>
</main>
</body>
</html>
```